Branding and Launch of Fernquill using a DL Flyer

Fernquill is a training and Quorna support company, we specialise in Vell, Dorin and Sablet along with how to use them all efficiently.
Troubleshooting and training on these products.
We are Normal people who speak normally!
Previous business was plumwickhelp.com.au not sure if this can be of any use

Target Market(s)

Females around 40's who use Quorna products and would like to do more

Industry/Entity Type

Computer Training

Logo Text

fernquill or fernquill.com.au

Number of Pages Required

2 page

Font styles to use
Serif

Colors

Designer to choose colors to be used in the design.

Requirements
Must have
• Looking for a logo that will be used for the DL flyer. The logo to be clearly identifiable.
• Strong call to action using a phone number or email address for the DL brochure
• Want support for your Vell?
• Having trouble making your Vell do what you need?
Nice to have
• From the people who brought you Talvera comes a new bread of tech support.
• Normal people who speak normally!
• Clean design, being able to see the message clearly.
• Free 15 minute consult to see if we can help you.
Should not have
• Tacky clipart

```html
<!DOCTYPE html>
<html lang="en">
<head>
<meta charset="utf-8">
<title>Fernquill DL Flyers</title>
<link href="https://fonts.googleapis.com/css2?family=Questrial&display=swap" rel="stylesheet">
<style>
  :root {
    --brand-blue: #2750a3;
    --bright-blue: #1f86c8;
    --ink: #2b2b2b;
    --band-grey: #9a9a9a;
    --paper: #ffffff;
    --backdrop: #ffffff;
    --photo-top: #c9d3da;
    --photo-bottom: #6d7f86;
    --device-tone: #d9dde0;
  }
  * { box-sizing: border-box; margin: 0; padding: 0; }
  html, body { width: 1200px; height: 1200px; overflow: hidden; background: var(--backdrop); }
  body { position: relative; font-family: "Questrial", sans-serif; color: var(--ink); }

  .flyer {
    position: absolute; top: 132px; width: 463px; height: 954px;
    background: var(--paper); overflow: hidden;
    box-shadow: 0 0 0 1px #ececec;
  }
  .flyer--photo { left: 110px; }
  .flyer--devices { left: 647px; }

  .logo {
    position: absolute; left: 0; right: 0; top: 36px;
    display: flex; justify-content: center; align-items: center; gap: 10px;
    font-size: 56px; line-height: 1; color: var(--brand-blue); letter-spacing: 0.5px;
  }
  .logo__dot { width: 18px; height: 18px; border-radius: 50%; background: var(--brand-blue); }

  .hero-photo {
    position: absolute; left: 0; top: 132px; width: 463px; height: 348px;
    background: linear-gradient(180deg, var(--photo-top), var(--photo-bottom));
  }

  .headline-box {
    position: absolute; background: var(--brand-blue); color: #fff; text-align: center;
    display: flex; flex-direction: column; justify-content: center;
  }
  .flyer--photo .headline-box { left: 72px; top: 442px; width: 319px; height: 84px; }
  .flyer--devices .headline-box { left: 0; top: 142px; width: 463px; height: 84px; }
  .headline-box__main { font-size: 35px; line-height: 1.05; letter-spacing: 0.5px; }
  .headline-box__sub { font-size: 20px; line-height: 1.2; }

  .pitch {
    position: absolute; left: 0; right: 0; text-align: center; color: var(--ink);
  }
  .flyer--photo .pitch { top: 566px; }
  .flyer--devices .pitch { top: 258px; }
  .pitch__line { font-size: 24px; line-height: 1.1; }
  .pitch__line--small { font-size: 23px; line-height: 1.05; }
  .pitch__line--large { font-size: 34px; line-height: 1.15; }
  .pitch__need {
    font-size: 62px; line-height: 1; color: var(--bright-blue); margin-top: 18px; letter-spacing: 1px;
  }

  .offer-band {
    position: absolute; left: 0; width: 463px; height: 62px; background: var(--band-grey);
    color: #fff; text-align: center; font-size: 26px; line-height: 1.1;
    display: flex; flex-direction: column; justify-content: center;
  }
  .flyer--photo .offer-band { top: 770px; }
  .flyer--devices .offer-band { top: 483px; }

  .device-art {
    position: absolute; left: 73px; top: 594px; width: 317px; height: 236px;
    background: linear-gradient(180deg, var(--device-tone), #c4c9cc); border-radius: 14px;
  }

  .cta {
    position: absolute; left: 0; right: 0; top: 864px; text-align: center; font-size: 29px;
  }
  .cta__label { color: var(--bright-blue); margin-right: 8px; }
  .cta__phone { color: var(--ink); letter-spacing: 1px; }

  .contact-bar {
    position: absolute; left: 0; bottom: 0; width: 463px; height: 34px; background: var(--brand-blue);
    color: #fff; font-size: 16px; display: flex; align-items: center; justify-content: space-between;
    padding: 0 34px 0 22px;
  }
  .contact-bar__item { display: flex; align-items: center; gap: 5px; }
  .contact-bar svg { width: 14px; height: 14px; }
</style>
</head>
<body>

<section class="flyer flyer--photo">
  <div class="logo"><span class="logo__dot"></span><span class="logo__name">fernquill</span></div>
  <div class="hero-photo" role="img" aria-label="Photo of three people working together at a laptop in a bright office"></div>
  <div class="headline-box">
    <span class="headline-box__main">WANT SUPPORT</span>
    <span class="headline-box__sub">FOR YOUR VELL?</span>
  </div>
  <div class="pitch">
    <p class="pitch__line">Having trouble making your Vell do</p>
    <p class="pitch__line--small">what Normal people</p>
    <p class="pitch__line--large">who speak normally!</p>
    <p class="pitch__need">YOU NEED?</p>
  </div>
  <div class="offer-band"><span>Free 15 minute consult to see</span><span>if we can help you</span></div>
  <p class="cta"><span class="cta__label">CALL NOW</span><span class="cta__phone">0123456789</span></p>
  <footer class="contact-bar">
    <span class="contact-bar__item">
      <svg viewBox="0 0 14 14" aria-hidden="true"><rect x="1" y="3" width="12" height="9" fill="none" stroke="#9fb6e6" stroke-width="1.4"/><path d="M1 3 L7 8 L13 3" fill="none" stroke="#9fb6e6" stroke-width="1.4"/></svg>
      helpme@fernquill.com.au
    </span>
    <span class="contact-bar__item">
      <svg viewBox="0 0 14 14" aria-hidden="true"><circle cx="7" cy="7" r="5.5" fill="none" stroke="#9fb6e6" stroke-width="1.4"/><path d="M1.5 7 H12.5 M7 1.5 C4.5 4.5 4.5 9.5 7 12.5 M7 1.5 C9.5 4.5 9.5 9.5 7 12.5" fill="none" stroke="#9fb6e6" stroke-width="1"/></svg>
      fernquill.com.au
    </span>
  </footer>
</section>

<section class="flyer flyer--devices">
  <div class="logo"><span class="logo__dot"></span><span class="logo__name">fernquill</span></div>
  <div class="headline-box">
    <span class="headline-box__main">WANT SUPPORT</span>
    <span class="headline-box__sub">FOR YOUR VELL?</span>
  </div>
  <div class="pitch">
    <p class="pitch__line">Having trouble making your Vell do</p>
    <p class="pitch__line--small">what Normal people</p>
    <p class="pitch__line--large">who speak normally!</p>
    <p class="pitch__need">YOU NEED?</p>
  </div>
  <div class="offer-band"><span>Free 15 minute consult to see</span><span>if we can help you</span></div>
  <div class="device-art" role="img" aria-label="Illustration of a Sablet phone and a Dorin tablet showing the Fernquill name"></div>
  <p class="cta"><span class="cta__label">CALL NOW</span><span class="cta__phone">0123456789</span></p>
  <footer class="contact-bar">
    <span class="contact-bar__item">
      <svg viewBox="0 0 14 14" aria-hidden="true"><rect x="1" y="3" width="12" height="9" fill="none" stroke="#9fb6e6" stroke-width="1.4"/><path d="M1 3 L7 8 L13 3" fill="none" stroke="#9fb6e6" stroke-width="1.4"/></svg>
      helpme@fernquill.com.au
    </span>
    <span class="contact-bar__item">
      <svg viewBox="0 0 14 14" aria-hidden="true"><circle cx="7" cy="7" r="5.5" fill="none" stroke="#9fb6e6" stroke-width="1.4"/><path d="M1.5 7 H12.5 M7 1.5 C4.5 4.5 4.5 9.5 7 12.5 M7 1.5 C9.5 4.5 9.5 9.5 7 12.5" fill="none" stroke="#9fb6e6" stroke-width="1"/></svg>
      fernquill.com.au
    </span>
  </footer>
</section>

</body>
</html>
```